Site Update/Merger: TWR Dynamics

We want to take some content (not ALL the content, but only what is specified) from two or our sites and combine into one
The New Website is in Wordpress too.
The new site needs to be a nice merge between these sites:
◦ https://brontavo-works.example/
◦ https://taskmira-launch.example/
Theme/topic: this is an Engineering site
The blog must be included on the home page (maybe smaller), and also on the Systems Engineering page (maybe a little bigger, allow the user to browse through all blogs)
Instructions and visual aids:
Step 1: SEE BRIEFING IN THE PDF ATTACHED
Step 2: some pictures for your reference (referenced in the PDF)

```html
<!DOCTYPE html>
<html lang="en">
<head>
<meta charset="utf-8">
<title>TWR Dynamics</title>
<link href="https://fonts.googleapis.com/css2?family=Saira:wght@400;500;600;700&family=Roboto:wght@400;500;700&display=swap" rel="stylesheet">
<style>
:root{
  --navy:#0b1633;
  --navy-2:#0f1e44;
  --blue:#1a8fd6;
  --blue-deep:#0d5fa6;
  --sky:#2fa6e8;
  --ink:#1b1f2a;
  --muted:#6b7280;
  --pale:#eef3f8;
  --white:#ffffff;
  --line:#d8dee6;
}
*{box-sizing:border-box;margin:0;padding:0}
html,body{width:1200px;height:2164px;overflow:hidden;background:var(--white)}
body{font-family:"Roboto",Arial,sans-serif;color:var(--ink);position:relative}
h1,h2,h3,.brand,.nav a{font-family:"Saira",Arial,sans-serif}

/* header */
.site-header{position:absolute;top:0;left:0;width:1200px;height:70px;z-index:5;display:flex;align-items:center;justify-content:space-between;padding:0 60px}
.brand{color:var(--white);font-size:34px;font-weight:600;letter-spacing:.5px}
.nav{display:flex;gap:44px;font-size:15px}
.nav a{color:var(--white);text-decoration:none;padding-bottom:6px;letter-spacing:.5px}
.nav a.active{border-bottom:2px solid var(--white)}

/* hero */
.hero{position:absolute;top:0;left:0;width:1200px;height:600px;
  background:linear-gradient(120deg,#06122c 0%,#0c2e66 45%,#1a6fc0 75%,#0b2450 100%);
  clip-path:polygon(0 0,100% 0,100% 86%,58% 100%,0 88%)}
.hero-copy{position:absolute;top:250px;left:60px;color:var(--white);z-index:2}
.hero-copy h1{font-size:44px;font-weight:600;letter-spacing:1px;margin-bottom:24px}
.hero-copy p{font-size:20px;line-height:1.45;width:560px;font-weight:500}

/* what we do */
.what-we-do{position:absolute;top:560px;left:0;width:1200px;height:210px;background:var(--pale);display:flex;align-items:center;padding:40px 60px 0}
.what-we-do h2{font-size:42px;font-weight:400;width:560px;color:var(--ink);letter-spacing:.5px}
.what-we-do h2 b{font-weight:700}
.what-we-do p{font-size:15px;line-height:1.5;width:500px;color:var(--ink)}

/* services intro */
.services-intro{position:absolute;top:780px;left:0;width:1200px;text-align:center}
.services-intro h2{font-size:44px;font-weight:400;letter-spacing:.5px}
.services-intro h2 b{font-weight:700}
.services-intro .rule{width:130px;height:2px;background:var(--ink);margin:6px auto 24px}
.services-intro p{font-size:15px;line-height:1.55;color:var(--muted);width:560px;margin:0 auto}

/* services panels */
.service-panels{position:absolute;top:940px;left:0;width:1200px;height:520px;display:flex}
.panel{width:600px;height:520px;padding:30px 60px;color:var(--white);text-align:center}
.panel-systems{background:var(--navy)}
.panel-physics{background:linear-gradient(135deg,var(--blue-deep),var(--sky))}
.panel-icon{width:90px;height:90px;border-radius:50%;margin:0 auto 18px;display:flex;align-items:center;justify-content:center}
.panel-systems .panel-icon{background:var(--blue)}
.panel-physics .panel-icon{background:rgba(255,255,255,.9)}
.panel h3{font-size:30px;font-weight:500;line-height:1.1;letter-spacing:.5px}
.panel .tagline{font-size:15px;margin:8px 0 26px;opacity:.85}
.panel-physics p{font-size:15px;line-height:1.7;width:420px;margin:22px auto 0;opacity:.95}
.focus-list{list-style:none;text-align:left;width:360px;margin:0 auto}
.focus-list li{display:flex;gap:18px;align-items:center;margin-bottom:22px}
.focus-list .dot{width:58px;height:58px;flex:none;border-radius:50%;background:var(--blue);display:flex;align-items:center;justify-content:center}
.focus-list strong{display:block;font-size:16px;font-weight:500;margin-bottom:2px}
.focus-list span{font-size:13px;opacity:.75;line-height:1.3;display:block}

/* blogs */
.latest-blogs{position:absolute;top:1490px;left:0;width:1200px;padding:0 100px}
.latest-blogs h2{font-size:44px;font-weight:400;letter-spacing:.5px}
.latest-blogs h2 b{font-weight:700}
.latest-blogs .rule{width:140px;height:2px;background:var(--ink);margin:4px 0 26px}
.blog-grid{display:flex;gap:28px}
.blog-card{width:315px;background:var(--white);box-shadow:0 2px 10px rgba(0,0,0,.12)}
.blog-thumb{height:185px}
.thumb-1{background:linear-gradient(135deg,#c9d2dc,#56667a)}
.thumb-2{background:linear-gradient(135deg,#0a2a55,#1b8fd8)}
.thumb-3{background:linear-gradient(135deg,#061a3a,#1a62b8)}
.blog-body{padding:18px 22px 22px}
.blog-date{font-size:11px;letter-spacing:.5px;color:var(--ink);margin-bottom:8px}
.blog-body h3{font-family:"Roboto",Arial,sans-serif;font-size:16px;font-weight:700;line-height:1.35;margin-bottom:10px}
.blog-body p{font-size:12px;line-height:1.5;color:var(--muted)}

/* footer */
.site-footer{position:absolute;top:2020px;left:0;width:1200px;height:144px;background:var(--navy-2);color:var(--white);padding:40px 100px;display:flex;justify-content:space-between}
.footer-nav{display:flex;gap:44px;font-size:14px}
.footer-social{display:flex;gap:10px;margin-top:16px}
.footer-social span{width:26px;height:26px;border:1px solid var(--white);border-radius:50%}
.copyright{font-size:12px;opacity:.8;padding-top:2px}
.contact{font-size:12px;line-height:1.8;opacity:.85}
</style>
</head>
<body>

<header class="site-header">
  <div class="brand">TWR Dynamics</div>
  <nav class="nav">
    <a class="active">HOME</a>
    <a>SERVICES ▾</a>
    <a>CONTACT US</a>
  </nav>
</header>

<section class="hero" role="img" aria-label="A hand touching a glowing blue circuit-board interface"></section>
<div class="hero-copy">
  <h1>WHO WE ARE</h1>
  <p>A Multi-Disciplinary Consulting and Engineering Service Provider for EV and Other Industries, with a Focus on Systematic Product Development</p>
</div>

<section class="what-we-do">
  <h2>WHAT <b>WE DO</b></h2>
  <p>A team of automotive, control and mechanical engineers from different industries and backgrounds and with more than 10 years of experience that came together to provide cost effective and specialized services to your organization or team in the pursue of your projects goals</p>
</section>

<section class="services-intro">
  <h2>OUR <b>SERVICES</b></h2>
  <div class="rule"></div>
  <p>This is just a glance at the activities and projects we can contribute to. For more details, go to our services menu or contact us to have a exploratory conversation.</p>
</section>

<section class="service-panels">
  <div class="panel panel-systems">
    <div class="panel-icon">
      <svg width="46" height="46" viewBox="0 0 46 46" fill="none" stroke="#fff" stroke-width="3"><circle cx="23" cy="23" r="8"/><circle cx="23" cy="23" r="17" stroke-dasharray="6 5"/></svg>
    </div>
    <h3>SYSTEMS ENGINEERING</h3>
    <div class="tagline">Our Focus: Collaboration, Accountability and Feedback</div>
    <ul class="focus-list">
      <li><div class="dot"><svg width="28" height="28" viewBox="0 0 28 28" fill="none" stroke="#fff" stroke-width="2"><circle cx="9" cy="10" r="4"/><circle cx="19" cy="10" r="4"/><path d="M2 24c1-5 13-5 14 0M12 24c1-5 13-5 14 0"/></svg></div><div><strong>Collaboration</strong><span>Working together is the only way to maximise the team's potential</span></div></li>
      <li><div class="dot"><svg width="28" height="28" viewBox="0 0 28 28" fill="none" stroke="#fff" stroke-width="2.5"><path d="M6 14l6 6 11-12"/></svg></div><div><strong>Accountability</strong><span>Individual contributions are paramount to the team's success</span></div></li>
      <li><div class="dot"><svg width="28" height="28" viewBox="0 0 28 28" fill="none" stroke="#fff" stroke-width="2"><path d="M4 5h20v13H12l-6 5v-5H4z"/></svg></div><div><strong>Feedback</strong><span>Clear feedback channels are in place</span></div></li>
    </ul>
  </div>
  <div class="panel panel-physics">
    <div class="panel-icon">
      <svg width="46" height="46" viewBox="0 0 46 46" fill="none" stroke="#1a8fd6" stroke-width="3"><rect x="8" y="12" width="30" height="20" rx="2"/><path d="M16 38h14M23 32v6"/></svg>
    </div>
    <h3>PHYSICS-BASED MODELING<br>AND HARDWARE IN THE LOOP</h3>
    <p>From data-driven system identification to machine-learning-based models for your simulation, we can handle that work for you. In addition, we are highly skilled on HIL testing and can support you to design and build a bench to test complex controller testing.</p>
  </div>
</section>

<section class="latest-blogs">
  <h2>LATEST <b>BLOGS</b></h2>
  <div class="rule"></div>
  <div class="blog-grid">
    <article class="blog-card">
      <div class="blog-thumb thumb-1" role="img" aria-label="Engineer working at a lab computer station"></div>
      <div class="blog-body">
        <div class="blog-date">20 SEPTEMBER</div>
        <h3>Fusce tellus Sed metus augue convallis et vehicula ut</h3>
        <p>Aenean dictum augue sed ipsum id tempus rutrum ornare nisl convallis.</p>
      </div>
    </article>
    <article class="blog-card">
      <div class="blog-thumb thumb-2" role="img" aria-label="Electric vehicle charging connector with glowing blue light"></div>
      <div class="blog-body">
        <div class="blog-date">20 SEPTEMBER</div>
        <h3>Fusce tellus Sed metus augue convallis et vehicula ut</h3>
        <p>Aenean dictum augue sed ipsum id tempus rutrum ornare nisl convallis.</p>
      </div>
    </article>
    <article class="blog-card">
      <div class="blog-thumb thumb-3" role="img" aria-label="Digital circuit and data interface in blue tones"></div>
      <div class="blog-body">
        <div class="blog-date">20 SEPTEMBER</div>
        <h3>Fusce tellus Sed metus augue convallis et vehicula ut</h3>
        <p>Aenean dictum augue sed ipsum id tempus rutrum ornare nisl convallis.</p>
      </div>
    </article>
  </div>
</section>

<footer class="site-footer">
  <div>
    <div class="footer-nav"><span>HOME</span><span>SERVICES</span><span>CONTACT US</span></div>
    <div class="footer-social"><span></span><span></span><span></span><span></span></div>
  </div>
  <div class="copyright">TWR DYNAMICS © 2020 ALL RIGHTS RESERVED</div>
  <div class="contact">North America Location: Northfield, OR<br>Email: info@twrdynamics.example</div>
</footer>

</body>
</html>
```